Singapore Lumivane website

Design a SEO friendly website

Target Market(s)

Adults with health challenges

Coding

Coded - Design and coding required

Number of Pages Required

5+ page

Requirements
Must have
• Free consultation form link to email response.
Information to be taken from our respective equipment suppliers websites as per file attached.

```html
<!DOCTYPE html>
<html lang="en">
<head>
<meta charset="utf-8">
<title>Singapore Lumivane – Total Wellness</title>
<link href="https://fonts.googleapis.com/css2?family=Fira+Sans:wght@400;500;600&family=Lato:wght@400;700&display=swap" rel="stylesheet">
<style>
:root{
  --teal:#5cbfd0;
  --teal-light:#7fd5d4;
  --teal-dark:#45acc4;
  --ink:#222;
  --text:#333;
  --grey-bg:#efefef;
  --orange:#ff5a10;
  --orange-light:#ff7a1a;
  --footer:#1d1f26;
  --white:#fff;
}
*{box-sizing:border-box;margin:0;padding:0}
html,body{width:1200px;height:3114px;overflow:hidden}
body{position:relative;font-family:"Lato",sans-serif;color:var(--text);background:var(--white)}
h1,h2,h3,.brand,.nav a{font-family:"Fira Sans",sans-serif}

/* header */
.site-header{position:absolute;left:0;top:0;width:1200px;height:97px}
.brand{position:absolute;left:75px;top:26px;font-size:34px;font-weight:600;color:var(--ink)}
.call{position:absolute;right:72px;top:22px;display:flex;align-items:center;gap:16px}
.call-icon{width:38px;height:38px;border-radius:50%;background:var(--ink);display:flex;align-items:center;justify-content:center}
.call small{display:block;color:var(--teal);font-size:14px;font-weight:700}
.call strong{display:block;font-family:"Fira Sans",sans-serif;font-size:28px;font-weight:500;color:var(--ink);line-height:1.1}

.nav{position:absolute;left:0;top:97px;width:1200px;height:49px;background:linear-gradient(90deg,var(--teal-dark),var(--teal-light));display:flex;padding-left:75px}
.nav a{color:var(--white);text-decoration:none;font-size:17px;font-weight:500;line-height:49px;padding:0 20px}
.nav a.active{background:#2a2a2a;padding:0 29px}

/* hero */
.hero-photo{position:absolute;left:0;top:146px;width:1200px;height:760px;background:linear-gradient(120deg,#8f9aa3 0%,#6d7d8a 35%,#a5b2bb 60%,#c9d2d8 100%)}
.hero-curve{position:absolute;left:0;top:800px}
.hero-title{position:absolute;left:75px;top:378px;font-size:57px;font-weight:600;color:var(--white)}
.hero-sub{position:absolute;left:75px;top:450px;font-family:"Fira Sans",sans-serif;font-size:25px;font-weight:500;color:var(--white);line-height:36px}
.btn{display:inline-block;width:186px;height:46px;line-height:46px;text-align:center;border-radius:23px;background:linear-gradient(90deg,var(--teal-light),var(--teal-dark));color:var(--white);font-family:"Fira Sans",sans-serif;font-size:17px;font-weight:500}
.hero-btn{position:absolute;left:75px;top:550px}
.dots{position:absolute;left:75px;top:632px;display:flex;gap:9px}
.dots i{width:12px;height:12px;border-radius:50%;background:var(--white)}
.dots i:first-child{background:#111}

.consult{position:absolute;left:794px;top:185px;width:332px;height:481px;background:rgba(255,255,255,.95);border-radius:10px;padding:16px 18px}
.consult h2{text-align:center;font-size:28px;font-weight:500;color:var(--ink);margin-bottom:12px}
.field{height:44px;border:1px solid #bbb;border-radius:22px;margin-bottom:12px;padding:0 20px;line-height:42px;font-size:14px;color:#333}
.field.msg{height:108px;line-height:1;padding-top:18px}
.submit{height:44px;border-radius:22px;background:linear-gradient(90deg,var(--orange),var(--orange-light));color:var(--white);text-align:center;line-height:44px;font-family:"Fira Sans",sans-serif;font-size:17px;font-weight:500}

/* pillars */
.pillar{position:absolute;width:242px;border-radius:8px;background:linear-gradient(180deg,var(--teal-light),var(--teal-dark));text-align:center;color:var(--white);padding-top:56px}
.pillar .icon{position:absolute;left:76px;top:-45px;width:90px;height:90px;border-radius:50%;background:var(--white);border:3px solid #e6f6f7;display:flex;align-items:center;justify-content:center}
.pillar h3{font-size:22px;font-weight:500}
.pillar b{display:block;font-size:14px;margin-top:6px}
.pillar p{font-size:15px;line-height:26px;margin-top:2px;padding:0 24px}
.pill-btn{display:inline-block;margin-top:8px;background:#111;color:var(--white);font-size:14px;font-weight:700;border-radius:15px;width:106px;height:29px;line-height:29px}

/* welcome */
.welcome{position:absolute;left:0;top:1099px;width:1200px;height:480px;background:var(--grey-bg);overflow:hidden}
.welcome h2{position:absolute;left:75px;top:54px;font-size:38px;font-weight:500;color:var(--ink);line-height:43px}
.welcome p{position:absolute;left:75px;top:160px;width:512px;font-size:15.5px;line-height:29.5px;color:#222}
.welcome .btn{position:absolute;left:75px;top:384px}
.welcome-photo{position:absolute;left:617px;top:-130px;width:740px;height:740px;border-radius:50%;background:linear-gradient(180deg,#e4a56a 0%,#c27c4a 35%,#4d5a4a 65%,#2f3a33 100%)}

/* methods */
.methods{position:absolute;left:0;top:1579px;width:1200px;height:703px}
.methods-band{position:absolute;left:0;top:0;width:1200px;height:334px;background:linear-gradient(90deg,var(--teal-dark),var(--teal-light))}
.methods h2{position:absolute;left:73px;top:60px;font-size:38px;font-weight:500;color:var(--white)}
.arrows{position:absolute;right:74px;top:66px;display:flex;gap:12px}
.arrows span{width:36px;height:36px;border:2px solid var(--white);display:flex;align-items:center;justify-content:center}
.method{position:absolute;top:141px;width:330px;height:492px;background:var(--white);border-radius:6px;box-shadow:0 2px 8px rgba(0,0,0,.15);overflow:hidden}
.method .photo{height:236px}
.method h3{margin:22px 0 0 18px;font-size:25px;font-weight:500;color:var(--teal)}
.method p{margin:6px 18px 0;font-size:15px;line-height:26px;color:#222}
.method .btn{position:absolute;left:22px;top:416px}

/* challenges */
.challenges{position:absolute;left:0;top:2282px;width:1200px;height:481px;background:var(--grey-bg);overflow:hidden}
.challenges-photo{position:absolute;left:-720px;top:-330px;width:1305px;height:1140px;border-radius:50%;background:linear-gradient(100deg,#b9b8b0 0%,#d2c8b8 45%,#3c6fb2 85%,#5d86c0 100%)}
.challenges h2{position:absolute;left:616px;top:50px;font-size:38px;font-weight:500;color:var(--ink)}
.challenges ul{position:absolute;left:616px;top:124px;width:510px;list-style:none}
.challenges li{position:relative;padding-left:33px;font-size:15px;line-height:26px;color:#222;margin-bottom:16px}
.challenges li svg{position:absolute;left:0;top:7px}
.challenges .btn{position:absolute;left:616px;top:377px}

/* info band */
.info{position:absolute;left:0;top:2763px;width:1200px;height:165px;background:var(--teal-dark)}
.info-item{position:absolute;top:40px;display:flex;gap:18px;color:var(--white)}
.info-item .ring{width:44px;height:44px;border:2px solid var(--white);border-radius:50%;display:flex;align-items:center;justify-content:center;flex:none}
.info-item h3{font-size:20px;font-weight:500;margin-top:8px}
.info-item p{font-size:14px;line-height:24px;margin-top:4px}

/* footer */
.site-footer{position:absolute;left:0;top:2928px;width:1200px;height:186px;background:radial-gradient(ellipse at 50% 80%,#263242,var(--footer) 70%);color:var(--white);text-align:center}
.footer-nav{display:flex;justify-content:center;gap:40px;margin-top:46px}
.footer-nav a{color:var(--white);text-decoration:none;font-family:"Fira Sans",sans-serif;font-size:17px;font-weight:500}
.copyright{font-size:13px;margin-top:22px}
.social{display:flex;justify-content:center;gap:24px;margin-top:18px}
.social span{width:22px;height:22px;border-radius:50%;background:var(--white)}
</style>
</head>
<body>

<header class="site-header">
  <div class="brand">Singapore Lumivane</div>
  <div class="call">
    <div class="call-icon"><svg width="18" height="18" viewBox="0 0 24 24"><path fill="#fff" d="M6.6 10.8a15.1 15.1 0 0 0 6.6 6.6l2.2-2.2c.3-.3.7-.4 1-.2 1.1.4 2.3.6 3.6.6.6 0 1 .4 1 1V20c0 .6-.4 1-1 1A17 17 0 0 1 3 4c0-.6.4-1 1-1h3.5c.6 0 1 .4 1 1 0 1.3.2 2.5.6 3.6.1.3 0 .7-.2 1z"/></svg></div>
    <div><small>Call Us Today</small><strong>1-800-555-0142</strong></div>
  </div>
</header>

<nav class="nav">
  <a class="active">Home</a><a>About Us</a><a>Services</a><a>Methods of Treatment</a><a>Latest News</a><a>Testimonials</a><a>Careers</a><a>Contact Us</a>
</nav>

<section class="hero">
  <div class="hero-photo" role="img" aria-label="Patient reclining with EEG electrode cap during a brain scan"></div>
  <svg class="hero-curve" width="1200" height="120" viewBox="0 0 1200 120"><path fill="#fff" d="M0 25 Q600 160 1200 35 L1200 120 L0 120 Z"/></svg>
  <h1 class="hero-title">Singapore Lumivane</h1>
  <div class="hero-sub">Providing Total Wellness :<br>Physical, Mental, Emotional &amp; Brain Health</div>
  <a class="btn hero-btn">Read More</a>
  <div class="dots"><i></i><i></i><i></i><i></i></div>

  <form class="consult">
    <h2>Free Consulation</h2>
    <div class="field">Name</div>
    <div class="field">Email Address</div>
    <div class="field">Phone No</div>
    <div class="field">Subject</div>
    <div class="field msg">Message</div>
    <div class="submit">Submit Now</div>
  </form>

  <div class="pillar" style="left:75px;top:765px;height:228px">
    <div class="icon"><svg width="50" height="44" viewBox="0 0 50 44"><path d="M6 40h38M10 40l6-10h20" stroke="#555" stroke-width="3" fill="none"/><circle cx="30" cy="7" r="4" fill="#555"/><path d="M28 12l-6 10 6 4-2 10M26 16l8 4" stroke="#555" stroke-width="3" fill="none"/></svg></div>
    <h3>Physical</h3><b>Freedom of Movements</b><p>Ability to do anything you want.</p><span class="pill-btn">Read More</span>
  </div>
  <div class="pillar" style="left:345px;top:798px;height:227px">
    <div class="icon"><svg width="46" height="46" viewBox="0 0 46 46"><path d="M10 42V30C4 24 6 6 22 5c12 0 17 8 16 16l4 7h-4v6c0 3-2 4-5 4h-5v4z" fill="#555"/></svg></div>
    <h3>Mental</h3><b>Maximised Functions</b><p>Ability &amp; skills to perform</p><span class="pill-btn">Read More</span>
  </div>
  <div class="pillar" style="left:615px;top:765px;height:228px">
    <div class="icon"><svg width="54" height="40" viewBox="0 0 54 40"><path d="M2 18C12 4 38 4 50 18 38 32 14 32 2 18z" fill="none" stroke="#555" stroke-width="4"/><circle cx="26" cy="18" r="7" fill="#555"/><path d="M44 26c3 4 4 7 2 9-2 1-4-1-4-3 0-2 1-4 2-6z" fill="#555"/></svg></div>
    <h3>Emotional</h3><b>Fulfilled, Satisfied &amp; Happy</b><p>Calm, Regulated &amp; Mindful</p><span class="pill-btn">Read More</span>
  </div>
  <div class="pillar" style="left:885px;top:798px;height:227px">
    <div class="icon"><svg width="50" height="50" viewBox="0 0 50 50" fill="none" stroke="#555" stroke-width="2"><ellipse cx="25" cy="25" rx="14" ry="12"/><path d="M25 13v24M18 18c3 2 3 6 0 8M32 18c-3 2-3 6 0 8M4 25h4M42 25h4M25 4v4M25 42v4M10 10l3 3M37 37l3 3M40 10l-3 3M10 40l3-3"/></svg></div>
    <h3>Brain</h3><b>Emerging and Growing</b><p style="padding:0 12px">Traumatic brain injury, Degenerative cognitive skills</p><span class="pill-btn">Read More</span>
  </div>
</section>

<section class="welcome">
  <h2>Welcome to<br>Singapore Lumivane</h2>
  <p>The 21st century comes with very competitive social and economic pressures and expectations which translate to work and social stress affecting our quality of life. Most people are also living longer with improved healthcare and there will be a larger proportion of aging population in many countries. There is no comprehensive and holistic neuro health service which looks into the physical, mental and emotional well-being which has to be integrative for optimum living.</p>
  <a class="btn">Read More</a>
  <div class="welcome-photo" role="img" aria-label="Singapore city skyline at sunset"></div>
</section>

<section class="methods">
  <div class="methods-band"></div>
  <h2>Methods of Treatment</h2>
  <div class="arrows">
    <span><svg width="12" height="14" viewBox="0 0 12 14"><path d="M9 1L3 7l6 6" stroke="#fff" stroke-width="2" fill="none"/></svg></span>
    <span><svg width="12" height="14" viewBox="0 0 12 14"><path d="M3 1l6 6-6 6" stroke="#fff" stroke-width="2" fill="none"/></svg></span>
  </div>
  <article class="method" style="left:75px">
    <div class="photo" role="img" aria-label="Clinician positioning a TMS helmet on a seated patient" style="background:linear-gradient(135deg,#c8c3b8,#8e8a80 60%,#b9bcc0)"></div>
    <h3>Deep TMS</h3>
    <p>Our patented breakthrough treatment based on Deep TMS (Transcranial magnetic stimulation ) begins a new era in brain stimulation and research.</p>
    <a class="btn">Read More</a>
  </article>
  <article class="method" style="left:435px">
    <div class="photo" role="img" aria-label="Therapist guiding a patient through computer-assisted cognitive exercises" style="background:linear-gradient(135deg,#d9d6cf,#a7b09d 55%,#e2e5e2)"></div>
    <h3>Cognitive Therapy</h3>
    <p>A comprehensive and sophisticated system of software for &nbsp;computer- assisted cognitive rehabilitation. This practical tool assists the therapist..</p>
    <a class="btn">Read More</a>
  </article>
  <article class="method" style="left:796px">
    <div class="photo" role="img" aria-label="Patient wearing a virtual reality headset beside a doctor" style="background:linear-gradient(135deg,#e8e9ef,#c9c4d6 55%,#dfe6ee)"></div>
    <h3>Virtual Reality</h3>
    <p>Virtual Reality is a technology that is used to recreate synthetic environments that are real or imaginary. When the immersion takes place, the patients thus benefit.</p>
    <a class="btn">Read More</a>
  </article>
</section>

<section class="challenges">
  <div class="challenges-photo" role="img" aria-label="Nurse comforting an elderly couple at home"></div>
  <h2>Major Health Challenges</h2>
  <ul>
    <li><svg width="14" height="14" viewBox="0 0 14 14"><circle cx="7" cy="7" r="7" fill="#45acc4"/><path d="M4 7l2 2 4-4" stroke="#fff" stroke-width="1.6" fill="none"/></svg>5.8% of the adult population in Singapore suffered from Major Depressive Disorder.</li>
    <li><svg width="14" height="14" viewBox="0 0 14 14"><circle cx="7" cy="7" r="7" fill="#45acc4"/><path d="M4 7l2 2 4-4" stroke="#fff" stroke-width="1.6" fill="none"/></svg>Trauma is the 5th leading cause of death in Singapore and remains the leading cause of death in young adults. Traumatic brain injury (TBI) accounts for up to 75% of trauma-related deaths.</li>
    <li><svg width="14" height="14" viewBox="0 0 14 14"><circle cx="7" cy="7" r="7" fill="#45acc4"/><path d="M4 7l2 2 4-4" stroke="#fff" stroke-width="1.6" fill="none"/></svg>In Singapore, 3.65 percent of the resident population has had a stroke in the past. There are 26 new stroke cases every day.</li>
  </ul>
  <a class="btn">Read More</a>
</section>

<section class="info">
  <div class="info-item" style="left:75px">
    <span class="ring"><svg width="14" height="18" viewBox="0 0 14 18"><path d="M7 0a7 7 0 0 0-7 7c0 5 7 11 7 11s7-6 7-11a7 7 0 0 0-7-7zm0 9.5A2.5 2.5 0 1 1 7 4.5a2.5 2.5 0 0 1 0 5z" fill="#fff"/></svg></span>
    <div><h3>Address Info</h3><p>1207 Harbour Lane<br>Road,Glasgow, D07 41KL</p></div>
  </div>
  <div class="info-item" style="left:437px">
    <span class="ring"><svg width="16" height="16" viewBox="0 0 24 24"><path fill="#fff" d="M6.6 10.8a15.1 15.1 0 0 0 6.6 6.6l2.2-2.2c.3-.3.7-.4 1-.2 1.1.4 2.3.6 3.6.6.6 0 1 .4 1 1V20c0 .6-.4 1-1 1A17 17 0 0 1 3 4c0-.6.4-1 1-1h3.5c.6 0 1 .4 1 1 0 1.3.2 2.5.6 3.6.1.3 0 .7-.2 1z"/></svg></span>
    <div><h3>Contact Us</h3><p>1-800-555-0142<br>hello@lumivane-care.com</p></div>
  </div>
  <div class="info-item" style="left:795px">
    <span class="ring"><svg width="16" height="16" viewBox="0 0 24 24"><path fill="#fff" d="M6.6 10.8a15.1 15.1 0 0 0 6.6 6.6l2.2-2.2c.3-.3.7-.4 1-.2 1.1.4 2.3.6 3.6.6.6 0 1 .4 1 1V20c0 .6-.4 1-1 1A17 17 0 0 1 3 4c0-.6.4-1 1-1h3.5c.6 0 1 .4 1 1 0 1.3.2 2.5.6 3.6.1.3 0 .7-.2 1z"/></svg></span>
    <div><h3>Request Free Consultation</h3><p>Phasellus tempus quam lacinia<br>eros laoreet</p></div>
  </div>
</section>

<footer class="site-footer">
  <nav class="footer-nav"><a>Home</a><a>About Us</a><a>Services</a><a>Methods of Treatment</a><a>Latest News</a><a>Testimonials</a><a>Careers</a><a>Contact Us</a></nav>
  <p class="copyright">Copyright© 2020 Lumivane Care All Right Reserved. Privacy Policy</p>
  <div class="social" aria-label="Social media links"><span></span><span></span><span></span><span></span><span></span></div>
</footer>

</body>
</html>
```